Professional & attention grabbing.

A business card design, front and back. I already have a logo I will attach, but I am open to something new as well.
Things to include:
Name:
Title:
Phone:
Email:
Wanting something that is professional but attention grabbing.
Also we do a lot of work using drones on natural gas pipelines (leading the future)if you want to include any of that. I'm open to ideas.
Target Market(s)
Natural gas transmission industry / greenhouse gas mitigation industry
Industry/Entity Type
Business
Contact Information for Business Card
All details have been conveyed above.
Colors
Designer to choose colors to be used in the design.
Look and feel
Each slider illustrates characteristics of the customer's brand and the style your logo design should communicate.

```html
<!DOCTYPE html>
<html lang="en">
<head>
<meta charset="utf-8">
<title>Corvaline Inspections – Business Card</title>
<link href="https://fonts.googleapis.com/css2?family=Roboto:wght@400;500;700;900&display=swap" rel="stylesheet">
<style>
  :root {
    --bg: #4a4a4c;
    --card-dark: #1f1f21;
    --card-dark-2: #3a3a3d;
    --card-light: #ffffff;
    --red: #d41f1f;
    --ink: #2b2b2d;
  }
  * { margin: 0; padding: 0; box-sizing: border-box; }
  html, body { width: 1200px; height: 852px; overflow: hidden; }
  body {
    background: var(--bg);
    font-family: "Roboto", Arial, sans-serif;
    position: relative;
  }
  .card {
    position: absolute;
    width: 540px;
    height: 310px;
    border-radius: 16px;
    overflow: hidden;
  }
  /* Front */
  .card--front {
    left: 90px; top: 110px;
    background: linear-gradient(160deg, var(--card-dark-2) 0%, var(--card-dark) 60%, #151516 100%);
  }
  .card--front .brand {
    position: absolute; left: 150px; top: 98px;
    display: flex; align-items: center; gap: 12px;
  }
  .brand__mark { width: 22px; height: 22px; background: var(--red); }
  .brand__name {
    font-weight: 900; font-size: 34px; letter-spacing: 1px;
    line-height: 1; text-transform: uppercase;
  }
  .card--front .brand__name { color: #ffffff; }
  .card--front .stripe {
    position: absolute; left: 420px; right: 0; top: 108px; height: 12px;
    background: var(--red);
  }
  .card--front .tagline-band {
    position: absolute; left: 0; right: 0; top: 226px; height: 34px;
    background: var(--red);
    display: flex; align-items: center; justify-content: center;
  }
  .tagline { color: #ffffff; font-size: 15px; font-weight: 400; letter-spacing: 0.3px; }
  /* Back */
  .card--back {
    left: 570px; top: 432px;
    background: var(--card-light);
  }
  .back-artwork {
    position: absolute; left: 300px; top: 150px; right: 0; bottom: 0;
    background: linear-gradient(135deg, #3a3a3d 0%, var(--card-dark) 70%);
  }
  .card--back .brand { position: absolute; left: 40px; top: 92px; display: flex; align-items: center; gap: 10px; }
  .card--back .brand__name { color: var(--ink); font-size: 30px; }
  .person { position: absolute; left: 56px; top: 170px; }
  .person__name {
    color: var(--red); font-weight: 900; font-size: 24px; letter-spacing: 1px; text-transform: uppercase;
  }
  .person__title { color: var(--ink); font-size: 13px; font-weight: 500; margin-top: 2px; }
  .contact {
    position: absolute; right: 26px; top: 180px;
    list-style: none; text-align: right; color: #ffffff; font-size: 13px; line-height: 21px;
  }
  .contact li { display: flex; justify-content: flex-end; align-items: center; gap: 6px; }
  .contact svg { width: 11px; height: 11px; fill: #ffffff; }
</style>
</head>
<body>
  <section class="card card--front" aria-label="Card front">
    <div class="brand">
      <span class="brand__mark"></span>
      <span class="brand__name">Corvaline</span>
    </div>
    <div class="stripe"></div>
    <div class="tagline-band">
      <p class="tagline">Also we do a lot of work using drones on natural gas pipelines</p>
    </div>
  </section>

  <section class="card card--back" aria-label="Card back">
    <div class="back-artwork" role="img" aria-label="Decorative dark and red wave artwork"></div>
    <div class="brand">
      <span class="brand__mark"></span>
      <span class="brand__name">Corvaline</span>
    </div>
    <div class="person">
      <p class="person__name">Daniel Reyes</p>
      <p class="person__title">Managing Director</p>
    </div>
    <ul class="contact">
      <li>1300 555 018
        <svg viewBox="0 0 24 24"><path d="M6.6 10.8a15 15 0 0 0 6.6 6.6l2.2-2.2a1 1 0 0 1 1-.25 11.4 11.4 0 0 0 3.6.57 1 1 0 0 1 1 1V20a1 1 0 0 1-1 1A17 17 0 0 1 3 4a1 1 0 0 1 1-1h3.5a1 1 0 0 1 1 1c0 1.250.2 2.45.57 3.57a1 1 0 0 1-.25 1z"/></svg>
      </li>
      <li>www.corvaline.com
        <svg viewBox="0 0 24 24"><circle cx="12" cy="12" r="10" fill="none" stroke="#fff" stroke-width="2.4"/><path d="M2 12h20M12 2c3 3 3 17 0 20M12 2c-3 3-3 17 0 20" fill="none" stroke="#fff" stroke-width="2"/></svg>
      </li>
      <li>d.reyes@corvaline.com
        <svg viewBox="0 0 24 24"><path d="M2 5h20v14H2z" fill="none" stroke="#fff" stroke-width="2.4"/><path d="M2 5l10 8 10-8" fill="none" stroke="#fff" stroke-width="2.4"/></svg>
      </li>
    </ul>
  </section>
</body>
</html>
```